Hadley & Partners, LLC Business Card 2016

We need a new business card design for a very important trade show coming up.

We are a compliance Consulting Firm. Our clients are stock brokerage firms and investment advisers.

I would like our logo on both sides of the card.

Info in the front of the card shold include:

Logo
First & Last Name
Title
Office #
Cell #
Email
Company Address (42 W. Calloway St., Suite 300 Pasadena, CA 91417

Back of the card should include the logo and url: www.hadleypartnersgroup.com

Target Market(s)

Stock Brokerage Firms and Investment Advisers

Industry/Entity Type

Financial Service

Contact Information for Business Card

Marcus J. Pellew
President
42 W. Calloway St., Suite 300
Pasadena, CA 91417
O 626.555.0147 ext. 204
C 818.555.0193
Email: marcus@hadleypartnersgroup.com
www.hadleypartnersgroup.com

Requirements
Nice to have
• The back of the card could be black with the logo with the white letters.
• I do want the front of the card to at least have the color logo with the black "Hadley & Partners Lettering.

```html
<!DOCTYPE html>
<html lang="en">
<head>
<meta charset="utf-8">
<title>Hadley &amp; Partners, LLC — Business Card</title>
<link href="https://fonts.googleapis.com/css2?family=Cinzel:wght@500&family=Lato:wght@400;700&display=swap" rel="stylesheet">
<style>
  :root {
    --backdrop: #e7e5e1;
    --card-white: #f7f7f7;
    --ink-black: #15161b;
    --panel-dark: #2a2c34;
    --panel-mid: #33353e;
    --band-dark: #1c1d23;
    --brand-red: #c21f2a;
    --text-light: #f2f2f2;
    --text-muted: #8b8e98;
    --icon-grey: #4a4c54;
    --rule: #4d5060;
  }
  * { box-sizing: border-box; margin: 0; padding: 0; }
  html, body { width: 1200px; height: 891px; overflow: hidden; }
  body {
    background: var(--backdrop);
    font-family: "Lato", sans-serif;
    display: flex; flex-direction: column; align-items: center; justify-content: center;
    gap: 56px;
  }
  .card {
    position: relative; width: 600px; height: 343px; overflow: hidden;
    box-shadow: 0 10px 28px rgba(0,0,0,.22);
  }

  /* ---------- front ---------- */
  .card-front { background: var(--card-white); }
  .brand {
    position: absolute; display: flex; align-items: center; gap: 12px;
    font-family: "Cinzel", serif; font-weight: 500; letter-spacing: .04em;
  }
  .card-front .brand { left: 40px; top: 150px; color: var(--ink-black); font-size: 25px; }
  .brand-square { width: 22px; height: 22px; background: var(--brand-red); flex: none; }

  .name-band {
    position: absolute; left: 328px; top: 40px; right: 0; height: 76px;
    background: var(--ink-black); padding: 16px 0 0 26px;
  }
  .person-name { color: var(--text-light); font-size: 25px; font-weight: 400; letter-spacing: .01em; }
  .person-title { color: var(--text-muted); font-size: 10px; margin-top: 2px; }

  .contact-panel {
    position: absolute; left: 348px; top: 116px; right: 0; height: 174px;
    background: linear-gradient(160deg, var(--panel-mid), var(--panel-dark));
    padding: 22px 0 0 26px; color: var(--text-light); font-size: 11.5px; line-height: 1.35;
  }
  .contact-row { height: 48px; }
  .bottom-band {
    position: absolute; left: 268px; bottom: 0; right: 0; height: 53px;
    background: linear-gradient(180deg, var(--band-dark), #111216);
  }
  .icon-column {
    position: absolute; left: 310px; top: 136px; display: flex; flex-direction: column; gap: 28px;
  }
  .icon { width: 20px; height: 20px; }

  /* ---------- back ---------- */
  .card-back { background: linear-gradient(135deg, #1b1d24 0%, #262831 60%, #20222a 100%); }
  .card-back .brand { left: 0; right: 0; top: 140px; justify-content: center; color: var(--text-light); font-size: 32px; }
  .card-back .brand-square { width: 28px; height: 28px; }
  .rule { position: absolute; height: 1px; background: var(--rule); }
  .rule-top { left: 0; top: 100px; width: 200px; }
  .rule-bottom { right: 0; top: 243px; width: 200px; }
  .website { position: absolute; left: 0; right: 0; top: 205px; text-align: center; color: var(--text-muted); font-size: 12px; letter-spacing: .03em; }
</style>
</head>
<body>

  <section class="card card-front" aria-label="Business card front">
    <div class="brand"><span class="brand-square"></span>Hadley &amp; Partners</div>

    <div class="name-band">
      <p class="person-name">Marcus J. Pellew</p>
      <p class="person-title">President</p>
    </div>

    <div class="icon-column" aria-hidden="true">
      <svg class="icon" viewBox="0 0 20 20"><circle cx="10" cy="10" r="9" fill="none" stroke="var(--icon-grey)" stroke-width="1.4"/><path d="M7 5.5l2 2-1 1.2c.6 1.3 1.6 2.3 2.9 2.9l1.2-1 2 2-1.2 1.4C9.5 13.8 6.2 10.5 6 6.7z" fill="var(--icon-grey)"/></svg>
      <svg class="icon" viewBox="0 0 20 20"><circle cx="10" cy="10" r="9.5" fill="var(--icon-grey)"/><path d="M10 4.8a3.3 3.3 0 0 0-3.3 3.3c0 2.5 3.3 6.4 3.3 6.4s3.3-3.9 3.3-6.4A3.3 3.3 0 0 0 10 4.8zm0 4.6a1.3 1.3 0 1 1 0-2.6 1.3 1.3 0 0 1 0 2.6z" fill="#fff"/></svg>
      <svg class="icon" viewBox="0 0 20 20"><rect x="2.5" y="5" width="15" height="10" fill="var(--icon-grey)"/><path d="M2.5 5l7.5 6 7.5-6" fill="none" stroke="#fff" stroke-width="1.1"/></svg>
    </div>

    <div class="contact-panel">
      <p class="contact-row">O : 626.555.0147 ext. 204<br>C : 818.555.0193</p>
      <p class="contact-row">42 W. Calloway St., Suite 300<br>Pasadena, CA 91417</p>
      <p class="contact-row">marcus@hadleypartnersgroup.com</p>
    </div>
    <div class="bottom-band"></div>
  </section>

  <section class="card card-back" aria-label="Business card back">
    <div class="rule rule-top"></div>
    <div class="brand"><span class="brand-square"></span>Hadley &amp; Partners</div>
    <p class="website">www.hadleypartnersgroup.com</p>
    <div class="rule rule-bottom"></div>
  </section>

</body>
</html>
```